Design new Brackwater Asset business card 2016

We need a new business card for our company Brackwater Asset Partners. We are a niche Alternative Investment Fund Manager based in Chester, in the North West of the UK.We market our services to global institutions such as banks, insurance companies, pension funds, etc. as well as wealthy individuals. Our main markets are Europe (Germany\France\Switzerland), the US and parts of Asia.
The design needs to be in line with existing company branding. Life the assets we deal with, the business card might suggest, "niche\alternative" type of attributes - however, it needs to remain professional, clean and appropriate for our client base.
Our existing business card format with relevant factual information is included, along with logo and branding details.

Target Market(s)

We market our services to global institutions such as banks, insurance companies, pension funds, etc. as well as wealthy individuals.

Industry/Entity Type

Financial Service

Contact Information for Business Card

please see attached pdf for information on existing business card which we should aim to convey on your new design. However:
- the wording "Brackwater Asset Partners Ltd is Authorised and Regulated
by the Monetary Oversight Bureau. Registered No. 7139046" should be replaced with , "Brackwater Asset Partners Ltd is an Alternative Investment Fund Manager Authorised and Regulated by the Monetary Oversight Bureau. Registered No. 7139046"
- the "reception" word on reverse can be omitted.
- the "retail: www.toplivanex.co.uk" wording can be omitted.
- the QR code is not required in the new version.

Font styles to use
Serif
Sans Serif

Requirements
Must have
• information on current business card, subject to comments provided above.
Nice to have
• Use of areas of solid colour instead of large areas of white space might be nice to experiment with. However, still need to have the general look and feel of the brand as presented on our website www.bwfundco.co.uk
• If we had space for 3 bullet points describing what we do\who we are, this might be good to try out. e.g. alternative investment fund manager, longevity specialist, founded 1990.
• Also, we have a new tag line, "expertise with longevity" which might fit nicely somewhere on the business card.
Should not have
• - no QR code
• - should not use all the colours in our logo as it looks very garish! Using one or two colours with black\white etc, seems to work better.

```html
<!DOCTYPE html>
<html lang="en">
<head>
<meta charset="utf-8">
<title>Brackwater Asset Partners – Business Card</title>
<link rel="stylesheet" href="https://fonts.googleapis.com/css2?family=Open+Sans:wght@400;600;700&family=Libre+Baskerville:wght@400&display=swap">
<style>
  :root {
    --bg: #2a2a2c;
    --card: #050505;
    --gold: #b4a03a;
    --blue: #3db6ea;
    --mark-a: #c9a63a;
    --mark-b: #3db6ea;
    --mark-c: #e23a4a;
  }
  * { box-sizing: border-box; margin: 0; padding: 0; }
  html, body { width: 1200px; height: 900px; overflow: hidden; }
  body {
    background: var(--bg);
    font-family: "Open Sans", Arial, sans-serif;
    position: relative;
  }
  .card {
    position: absolute;
    width: 600px;
    height: 343px;
    background: var(--card);
    border-radius: 18px;
    box-shadow: 0 10px 30px rgba(0,0,0,.5);
    overflow: hidden;
  }
  .card--front { left: 50px; top: 60px; }
  .card--back { left: 550px; top: 490px; }

  /* Front: company info */
  .company-name {
    position: absolute; left: 36px; top: 86px;
    color: var(--gold); font-weight: 700; font-size: 22px; letter-spacing: .5px;
  }
  .mark-circle {
    position: absolute; left: 400px; top: 22px; width: 160px; height: 110px;
  }
  .founded {
    position: absolute; right: 40px; top: 140px;
    color: var(--blue); font-size: 15px;
  }
  .services {
    position: absolute; left: 36px; top: 188px; list-style: none;
  }
  .services li {
    color: var(--blue); font-size: 13px; line-height: 17px;
    display: flex; align-items: center; gap: 10px;
  }
  .services li::before {
    content: ""; width: 9px; height: 9px; border-radius: 50%; background: var(--gold);
  }
  .address {
    position: absolute; left: 36px; top: 250px;
    color: var(--gold); font-size: 12.5px;
  }
  .website {
    position: absolute; left: 36px; top: 268px;
    color: var(--blue); font-size: 12.5px;
  }
  .website span { color: var(--gold); }
  .legal {
    position: absolute; left: 36px; top: 292px; width: 540px;
    color: var(--blue); font-size: 11px; line-height: 15px;
  }

  /* Back: personal details */
  .mark-large {
    position: absolute; left: 60px; top: 60px; width: 230px; height: 220px;
  }
  .divider {
    position: absolute; left: 315px; top: 60px; width: 1.5px; height: 230px;
    background: var(--blue);
  }
  .brand-name {
    position: absolute; left: 335px; top: 72px;
    font-family: "Libre Baskerville", Georgia, serif;
    color: var(--gold); font-size: 17px; line-height: 22px;
  }
  .tagline {
    position: absolute; left: 335px; top: 124px;
    font-family: "Libre Baskerville", Georgia, serif;
    color: var(--blue); font-size: 10.5px; letter-spacing: .6px;
  }
  .person-name {
    position: absolute; left: 335px; top: 148px;
    color: var(--blue); font-weight: 700; font-size: 22px;
  }
  .person-role {
    position: absolute; left: 335px; top: 178px;
    color: var(--gold); font-size: 13px;
  }
  .contacts {
    position: absolute; left: 335px; top: 210px; list-style: none;
  }
  .contacts li {
    display: flex; align-items: center; gap: 9px;
    color: var(--gold); font-size: 13px; line-height: 19px;
  }
  .contacts svg { width: 12px; height: 12px; fill: none; stroke: var(--blue); stroke-width: 1.6; }
</style>
</head>
<body>

<section class="card card--front">
  <div class="company-name">BRACKWATER ASSET PARTNERS</div>
  <svg class="mark-circle" role="img" aria-label="Brand emblem area" viewBox="0 0 160 110">
    <defs>
      <radialGradient id="markFront" cx="50%" cy="50%" r="60%">
        <stop offset="0" stop-color="#c9a63a"/>
        <stop offset=".55" stop-color="#d24a60"/>
        <stop offset="1" stop-color="#3db6ea"/>
      </radialGradient>
    </defs>
    <ellipse cx="80" cy="55" rx="78" ry="53" fill="url(#markFront)"/>
  </svg>
  <div class="founded">Founded 1990.</div>
  <ul class="services">
    <li>Alternative Investment</li>
    <li>Fund Manager</li>
    <li>Longevity Specialist</li>
  </ul>
  <div class="address">4-6 Ashdown Yard | Mercer Lane | Chester | CH2 9QX | UK</div>
  <div class="website">www.bwfundco<span>.co.uk</span></div>
  <p class="legal">Brackwater Asset Partners Ltd is an Alternative Investment Fund Manager Authorised and Regulated by the Monetary Oversight Bureau. Registered No. 7139046</p>
</section>

<section class="card card--back">
  <svg class="mark-large" role="img" aria-label="Brand emblem area" viewBox="0 0 230 220">
    <defs>
      <radialGradient id="markBack" cx="50%" cy="50%" r="60%">
        <stop offset="0" stop-color="#c9a63a"/>
        <stop offset=".55" stop-color="#d24a60"/>
        <stop offset="1" stop-color="#3db6ea"/>
      </radialGradient>
    </defs>
    <ellipse cx="115" cy="110" rx="113" ry="108" fill="url(#markBack)"/>
  </svg>
  <div class="divider"></div>
  <div class="brand-name">Brackwater Asset<br>Partners</div>
  <div class="tagline">EXPERTISE WITH LONGEVITY</div>
  <div class="person-name">MARTIN HALE</div>
  <div class="person-role">Non-Executive Chairman</div>
  <ul class="contacts">
    <li><svg viewBox="0 0 12 12"><path d="M2 8 Q6 4 10 8 M3 8 h6 v3 h-6 z"/></svg>+44 (0)1632 960418</li>
    <li><svg viewBox="0 0 12 12"><rect x="3" y="1" width="6" height="10" rx="1"/><path d="M5 9.5 h2"/></svg>+44 (0)7700 900514</li>
    <li><svg viewBox="0 0 12 12"><rect x="1" y="3" width="10" height="7"/><path d="M1 3 L6 7 L11 3"/></svg>mhale@bwfundco.co.uk</li>
  </ul>
</section>

</body>
</html>
```